Exec Conference Design Concept

We need to refresh & update nonprofit association graphic design for annual meeting. The graphics will be used to promote the event primarily through digital communications & social media. Other materials we generate for this event are the agenda & billboard content. You can view the existing design at www.lumivarguild.org under Events.

The target audience is primarily male, ages 35-60 in executive positions in C-Corps. The conference topics center on manufacturing regulations, marketing trends, and the economy. This conference has been around almost 30 years so we need something to invigorate potential registrants that will get their attention. It still needs to be professional and business-like.

In addition to a new design concept we would like to update the color palette. We’ve attached some mood boards with potential color & font suggestions. Our company logo is also attached and is the only design element tied to our branding that cannot be changed.

Designs should be energetic and sophisticated. Ideally, we would like the designs in Adobe Indesign or Photoshop. However, we can work with Illustrator.

Target Market(s)

Male business executives age 35-60.

Industry/Entity Type

Polystyrene manufacturing industry supply chain.

Font styles to use
Other font styles liked:
• I usually prefer sans serif

Requirements
Must have
• Focus points to draw attention to higher level informational units. For example, some people will only read the headers and not detailed copy.
Nice to have
• Ways to insert bonus content that don’t over power other content. I like to see a good use of white space to enhance readability.

```html
<!DOCTYPE html>
<html lang="en">
<head>
<meta charset="utf-8">
<title>Lumivar Expo 2026 – Navigating the Business of Tomorrow</title>
<link rel="stylesheet" href="https://fonts.googleapis.com/css2?family=Barlow+Condensed:wght@300;400;500;600;700&family=Montserrat:wght@400;500&display=swap">
<style>
  :root{
    --stage:#ececec;
    --paper:#ffffff;
    --ink:#111412;
    --night:#0d110e;
    --bronze:#a35d18;
    --olive:#9db04a;
    --lime:#8db61e;
    --photo-light:#e4e2dc;
    --photo-mid:#b9b6ae;
    --photo-deep:#3e4a58;
  }
  *{margin:0;padding:0;box-sizing:border-box}
  html,body{width:766px;height:1200px;overflow:hidden;background:var(--stage)}
  .flyer{position:absolute;left:52px;top:0;width:661px;height:1200px;background:var(--paper);overflow:hidden;font-family:"Barlow Condensed",sans-serif;color:var(--ink)}
  .brand{position:absolute;left:0;width:100%;top:88px;display:flex;justify-content:center;align-items:center;gap:10px}
  .brand-square{width:38px;height:38px;background:var(--lime);border-radius:6px}
  .brand-name{font-weight:700;font-size:34px;line-height:1;color:#4a2a12;letter-spacing:.5px}
  .headline{position:absolute;left:88px;top:186px;font-weight:700;font-size:56px;line-height:47px;letter-spacing:-.3px;text-transform:uppercase}
  .headline-row{display:flex;align-items:center;gap:20px;white-space:nowrap}
  .event-tag{border:1.5px solid var(--bronze);color:var(--bronze);font-weight:400;font-size:26px;line-height:1;padding:4px 8px 3px;letter-spacing:.2px}
  .event-tag strong{font-weight:700}
  .tagline{position:absolute;left:88px;width:484px;top:300px;font-weight:600;font-size:19.5px;letter-spacing:.1px;text-transform:uppercase;text-align:center;white-space:nowrap}
  .rule{position:absolute;left:0;width:100%;background:var(--bronze)}
  .rule-top{top:356px;height:10px}
  .rule-bottom{top:1191px;height:9px}
  .hero-photo{position:absolute;left:0;top:366px;width:100%;height:304px;background:linear-gradient(100deg,var(--photo-mid) 0%,var(--photo-light) 30%,#4b525a 38%,#5a6068 50%,var(--photo-light) 62%,#f1f0ec 80%,var(--photo-deep) 100%)}
  .topics{position:absolute;left:0;top:670px;width:100%;height:259px;background:var(--night);display:grid;grid-template-columns:210px 210px 210px;padding-left:30px}
  .topic{padding-top:14px;display:flex;flex-direction:column;align-items:center}
  .topic-icon{width:48px;height:48px}
  .topic-title{margin-top:12px;color:var(--bronze);font-weight:700;font-size:24px;line-height:23px;text-align:center;text-transform:uppercase}
  .topic-points{margin-top:17px;list-style:none;font-family:"Montserrat",sans-serif;font-size:10.5px;line-height:12.5px;color:#f2f2f2;border-left:1px solid #5c3a18;padding-left:9px;width:150px;align-self:center;margin-left:22px}
  .topic-points li{position:relative;margin-bottom:8px}
  .topic-points li::before{content:"";position:absolute;left:-12px;top:3px;width:5px;height:5px;border-radius:50%;background:var(--bronze)}
  .cta{position:absolute;left:185px;top:903px;width:290px;height:55px;border-radius:18px;background:var(--olive);color:#fff;font-weight:600;font-size:31px;line-height:55px;text-align:center;letter-spacing:.3px;text-decoration:none}
  .bonus{position:absolute;left:47px;top:987px;width:566px;height:131px;border:2px solid var(--ink)}
  .bonus-corner{position:absolute;right:-2px;top:-2px;width:36px;height:36px}
  .bonus-thumb{position:absolute;left:28px;top:26px;width:112px;height:82px;background:var(--night);overflow:hidden}
  .thumb-mark{position:absolute;left:10px;top:14px;width:14px;height:10px;background:var(--lime)}
  .thumb-text{position:absolute;left:10px;top:34px;color:#fff;font-weight:500;font-size:7.5px;line-height:8.5px;text-transform:uppercase}
  .thumb-url{position:absolute;left:10px;top:70px;color:#cfcfcf;font-size:4px}
  .thumb-photo{position:absolute;right:0;top:0;width:30px;height:82px;background:linear-gradient(180deg,#2f5fa8,#8fa0b0 60%,#c8c6c0);border-left:3px solid var(--lime);border-radius:30px 0 0 0}
  .bonus-title{position:absolute;left:174px;top:20px;font-weight:600;font-size:24px;line-height:1;text-transform:uppercase;white-space:nowrap}
  .bonus-copy{position:absolute;left:175px;top:48px;width:372px;font-family:"Montserrat",sans-serif;font-size:11px;line-height:13.5px}
  .bonus-link{position:absolute;left:175px;top:86px;font-family:"Montserrat",sans-serif;font-weight:500;font-size:14px;color:var(--ink);text-decoration:underline;text-underline-offset:2px}
  .footer{position:absolute;left:0;top:1132px;width:100%;height:59px;background:var(--night)}
  .social{position:absolute;left:47px;top:19px;display:flex;gap:7px}
  .social span{width:21px;height:21px;border-radius:50%;background:#fff;display:block}
  .contact{position:absolute;right:48px;top:18px;color:#fff;font-weight:400;font-size:14.5px;letter-spacing:.6px}
</style>
</head>
<body>
<main class="flyer">
  <div class="brand"><span class="brand-square"></span><span class="brand-name">LUMIVAR EXPO 2026</span></div>

  <h1 class="headline">
    <div class="headline-row">Navigating the Business</div>
    <div class="headline-row">Of Tomorrow <span class="event-tag">LUMIVAR EXPO <strong>2026</strong></span></div>
  </h1>
  <p class="tagline">Decades of leadership, reimagined for the modern executive</p>

  <div class="rule rule-top"></div>
  <div class="hero-photo" role="img" aria-label="Photo of a worker measuring a large white foam block with a tape measure in a warehouse"></div>

  <section class="topics">
    <article class="topic">
      <svg class="topic-icon" viewBox="0 0 48 48" fill="none" stroke="#fff" stroke-width="1.6">
        <path d="M21 3h6l1 5 4 2 4-3 4 4-3 4 2 4 5 1v6l-5 1-2 4 3 4-4 4-4-3-4 2-1 5h-6l-1-5-4-2-4 3-4-4 3-4-2-4-5-1v-6l5-1 2-4-3-4 4-4 4 3 4-2z"/>
        <circle cx="24" cy="24" r="12"/>
        <line x1="16" y1="16" x2="32" y2="32"/>
        <circle cx="20" cy="26" r="2.5"/><circle cx="27" cy="21" r="2.5"/>
      </svg>
      <h2 class="topic-title">Manufacturing<br>Regulations</h2>
      <ul class="topic-points"><li>Compliance in a changing world</li><li>Policy impact on production</li></ul>
    </article>
    <article class="topic">
      <svg class="topic-icon" viewBox="0 0 60 48" fill="none" stroke="#fff" stroke-width="1.6">
        <path d="M8 18h10l18-10v30L18 30H8z"/>
        <path d="M12 30l3 12h6l-3-12"/>
        <path d="M36 12c6 2 6 18 0 22"/>
        <line x1="46" y1="22" x2="52" y2="22"/><line x1="44" y1="12" x2="49" y2="8"/><line x1="44" y1="32" x2="49" y2="36"/>
      </svg>
      <h2 class="topic-title">Marketing<br>Trends</h2>
      <ul class="topic-points"><li>Data-driven customer growth</li><li>Digital transformation strategies</li></ul>
    </article>
    <article class="topic">
      <svg class="topic-icon" viewBox="0 0 48 48" fill="none" stroke="#fff" stroke-width="1.6">
        <rect x="6" y="30" width="6" height="14"/><rect x="15" y="24" width="6" height="20"/><rect x="24" y="27" width="6" height="17"/><rect x="33" y="16" width="6" height="28"/>
        <path d="M4 24l11-8 9 6 16-14"/><path d="M34 8h6v6"/>
      </svg>
      <h2 class="topic-title">Economic<br>Outlook</h2>
      <ul class="topic-points"><li>Market risks and opportunities</li><li>Forecasting industry growth</li></ul>
    </article>
  </section>

  <a class="cta" href="#">REGISTER TODAY</a>

  <aside class="bonus">
    <svg class="bonus-corner" viewBox="0 0 36 36"><path d="M0 0h36v36z" fill="#0d110e"/></svg>
    <div class="bonus-thumb">
      <span class="thumb-mark"></span>
      <p class="thumb-text">Download our<br>exclusive monthly<br>newsletter</p>
      <p class="thumb-url">www.lumivarguild.org</p>
      <div class="thumb-photo" role="img" aria-label="Photo of factory machinery"></div>
    </div>
    <h3 class="bonus-title">Bonus Content: Executive Insights</h3>
    <p class="bonus-copy">Exclusive insights from industry leaders to help you navigate change, adapt faster, and stay ahead.</p>
    <a class="bonus-link" href="#">Download Our Exclusive Monthly Newsletter</a>
  </aside>

  <footer class="footer">
    <div class="social"><span></span><span></span><span></span></div>
    <p class="contact">(555) 014-2290 &nbsp;|&nbsp; www.lumivarguild.org</p>
  </footer>
  <div class="rule rule-bottom"></div>
</main>
</body>
</html>
```